Steadfast sons flyer

Benefits of prayer
- Prayer connects you to the God of fullness. Gal. 6:8
- Prayer places you cares on the Lord. 1 Peter 5:7, Matt. 11:28
- Prayer makes you fruitful in the vineyard of the Lord-this brings honour and glory. John 15:2
- Through prayer you exercise your Kingly authority. Matt. 16:19, 18:19.
- Prayer transforms you to be like Him. Luke 9:29.
- Prayer quickens divine inheritance. Luke 5:3-6
- Prayer will stir divine potentials in you. 2 Tim. 1:6
- And many more!

Experience the might and possibilities of prayer.

Join the Steadfast Sons Ministry!

```html
<!DOCTYPE html>
<html lang="en">
<head>
<meta charset="utf-8">
<title>Steadfast Sons Ministry – Flyer</title>
<link href="https://fonts.googleapis.com/css2?family=Parisienne&family=Noto+Sans:wght@400&display=swap" rel="stylesheet">
<style>
  :root {
    --page-bg: #eef0f4;
    --paper: #ffffff;
    --ink-blue: #1c22a8;
    --panel-blue: #0b2fa0;
    --band-green: #66cc00;
    --list-ink: #ffffff;
    --panel-glow: rgba(255,255,255,0.13);
  }
  * { margin: 0; padding: 0; box-sizing: border-box; }
  html, body {
    width: 1200px; height: 1000px; overflow: hidden;
    background: var(--page-bg);
  }
  .flyer {
    position: absolute; left: 211px; top: 0;
    width: 778px; height: 1000px;
    background: var(--paper);
    overflow: hidden;
  }
  .flyer-title {
    position: absolute; left: 30px; right: 30px; top: 52px;
    text-align: center;
    white-space: nowrap;
    font-family: "Parisienne", cursive;
    font-weight: 400; font-size: 49px;
    color: var(--ink-blue);
  }
  .benefits-panel {
    position: absolute; left: 22px; top: 144px;
    width: 734px; height: 493px;
    background: var(--band-green);
    padding: 25px 0;
  }
  .benefits-body {
    position: relative; height: 100%;
    background: var(--panel-blue);
    overflow: hidden;
  }
  .panel-backdrop {
    position: absolute; left: 300px; top: 20px;
    width: 360px; height: 420px;
    background: radial-gradient(ellipse at center, var(--panel-glow) 0%, rgba(255,255,255,0) 70%);
  }
  .benefits-heading {
    position: relative;
    padding: 28px 0 0 30px;
    font-family: "Parisienne", cursive;
    font-weight: 400; font-size: 46px;
    color: var(--list-ink);
  }
  .benefits-list {
    position: relative;
    list-style: none;
    margin: 16px 0 0 42px;
    width: 620px;
    font-family: "Noto Sans", sans-serif;
    font-size: 19.5px; line-height: 28px;
    color: var(--list-ink);
  }
  .benefits-list li {
    padding-left: 38px; text-indent: -16px;
  }
  .benefits-list li::before { content: "- "; }
  .flyer-tagline {
    position: absolute; left: 0; right: 0; top: 662px;
    text-align: center;
    font-family: "Parisienne", cursive;
    font-size: 38px; line-height: 56px;
    color: var(--ink-blue);
  }
  .fellowship-mark {
    position: absolute; left: 0; right: 0; top: 850px;
    display: flex; align-items: center; justify-content: center; gap: 16px;
  }
  .fellowship-dot {
    width: 76px; height: 76px; border-radius: 50%;
    background: var(--band-green);
  }
  .fellowship-name {
    font-family: "Parisienne", cursive;
    font-size: 40px;
    color: var(--ink-blue);
  }
</style>
</head>
<body>
  <main class="flyer">
    <h1 class="flyer-title">Join the Steadfast Sons Ministry!</h1>

    <section class="benefits-panel">
      <div class="benefits-body">
        <div class="panel-backdrop" role="img" aria-label="Faint cross motif behind the list"></div>
        <h2 class="benefits-heading">Benefits of prayer</h2>
        <ul class="benefits-list">
          <li>Prayer connects you to the God of fullness. Gal. 6:8</li>
          <li>Prayer places you cares on the Lord. 1 Peter 5:7, Matt. 11:28</li>
          <li>Prayer makes you fruitful in the vineyard of the Lord-this brings honour and glory. John 15:2</li>
          <li>Through prayer you exercise your Kingly authority. Matt. 16:19, 18:19.</li>
          <li>Prayer transforms you to be like Him. Luke 9:29.</li>
          <li>Prayer quickens divine inheritance. Luke 5:3-6</li>
          <li>Prayer will stir divine potentials in you. 2 Tim. 1:6</li>
          <li>And many more!</li>
        </ul>
      </div>
    </section>

    <p class="flyer-tagline">Experience the might and<br>possibilities of prayer.</p>

    <div class="fellowship-mark">
      <span class="fellowship-dot"></span>
      <span class="fellowship-name">Sons of Hope Fellowship</span>
    </div>
  </main>
</body>
</html>
```